Brochure for TrekPulse software for fleets

Hi. I want to create a top quality brochure with a tidy layout, easy to follow and understand. The brochure will be sent to companies who operate fleets of vans etc. to tell them our fuel savings 'TrekPulse' product/service. I have attached relevant info and imagery, now I need the final product to be 100% professional.
Important info to be made clear:
1. Guaranteed fuel savings
2. Minimizes inefficient driving habits by your employee
3. reducing wear on the vehicle
I will have upcoming projects for flyers, packaging etc.
Thank you
Colin
Target Market(s)
fleet operators - any motorists who want better efficiency from their vehicle
Industry/Entity Type
Software
Font styles to use
Look and feel
Each slider illustrates characteristics of the customer's brand and the style your logo design should communicate.

```html
<!DOCTYPE html>
<html lang="en">
<head>
<meta charset="utf-8">
<title>TrekPulse Fleet Brochure</title>
<link href="https://fonts.googleapis.com/css2?family=Lato:wght@400;700;900&family=Montserrat:wght@600;700&display=swap" rel="stylesheet">
<style>
:root{
  --blue:#1a8fd1;
  --blue-light:#c8e6f5;
  --charcoal:#3d4447;
  --grey:#6f7476;
  --gold:#f0bb1e;
  --gold-soft:#f5cf55;
  --white:#ffffff;
  --ink:#222628;
  --stage:#ece6e2;
}
*{box-sizing:border-box;margin:0;padding:0}
html,body{width:1200px;height:1200px;overflow:hidden}
body{background:var(--stage);font-family:"Lato",sans-serif;color:var(--ink);position:relative}
.spread{position:absolute;width:760px;height:537px;display:flex;box-shadow:0 6px 18px rgba(0,0,0,.18)}
.spread--covers{left:40px;top:24px}
.spread--inside{left:400px;top:630px}
.page{position:relative;width:380px;height:537px;background:var(--white);overflow:hidden}
.page + .page{border-left:1px solid #e2e2e2}
.abs{position:absolute}
.label{position:absolute;font-family:"Lato",sans-serif;font-weight:700;font-size:38px;line-height:1;letter-spacing:.5px;color:#111;white-space:nowrap}
.brand{display:flex;align-items:center;gap:6px;font-family:"Montserrat",sans-serif;font-weight:700;color:var(--charcoal);letter-spacing:2px;white-space:nowrap}
.brand__mark{width:14px;height:14px;background:var(--blue);flex:none}
.tagline{font-size:6px;color:var(--blue);letter-spacing:1px;text-transform:uppercase}
.contact{font-size:10px;line-height:1.45;color:var(--grey);text-align:center}
.contact p + p{margin-top:10px}
.photo{position:absolute}
.title-box{font-family:"Montserrat",sans-serif;color:var(--charcoal);text-align:center;font-weight:700;line-height:1.05}
.product{font-family:"Montserrat",sans-serif;font-weight:700;color:var(--white)}
.product__name{display:inline-block;background:var(--charcoal);padding:3px 8px;border-radius:3px;font-size:11px}
.small{font-size:7px;line-height:1.4}
.body-copy{font-size:8.4px;line-height:1.45;color:var(--ink)}
.body-copy ul{margin:6px 0 6px 12px}
.col-head{font-weight:700;font-size:10px;margin-bottom:5px}
.tech-list{font-size:7px;line-height:1.35;color:var(--white);list-style:none}
.tech-list li{margin-bottom:3px}
.caption{font-family:"Montserrat",sans-serif;font-weight:700;color:var(--white);text-transform:uppercase}
</style>
</head>
<body>

<section class="spread spread--covers">
  <article class="page page--back">
    <div class="abs" style="left:0;top:80px;width:300px;height:410px;background:var(--blue)"></div>
    <div class="abs" style="left:0;top:96px;width:284px;height:378px;background:var(--blue-light)"></div>
    <div class="abs" style="left:0;top:96px;width:284px;height:112px;background:var(--white)"></div>
    <div class="abs" style="left:300px;top:40px;width:80px;height:330px;background:var(--charcoal)"></div>
    <div class="abs" style="left:250px;top:270px;width:50px;height:150px;background:var(--blue)"></div>
    <div class="abs brand" style="left:86px;top:134px;font-size:20px"><span class="brand__mark"></span>CORVANE</div>
    <div class="abs tagline" style="left:108px;top:162px">Remapping Solutions</div>
    <div class="abs contact" style="left:40px;top:250px;width:200px">
      <p>Office address:<br>Corvane Technologies Ltd<br>Harbour House<br>Westfield Business Park<br>Millbrook<br>Co.Westmeath</p>
      <p>Telephone:<br>01 555 0182</p>
      <p>Website:<br>www.corvane.example</p>
    </div>
  </article>

  <article class="page page--front">
    <div class="abs" style="left:0;top:150px;width:110px;height:280px;background:var(--blue)"></div>
    <div class="abs" style="left:0;top:200px;width:60px;height:230px;background:var(--charcoal)"></div>
    <div class="abs brand" style="left:12px;top:72px;font-size:12px;gap:5px"><span class="brand__mark" style="width:9px;height:9px"></span>CORVANE</div>
    <div class="abs tagline" style="left:26px;top:90px;font-size:5px">Remapping Solutions</div>
    <div class="abs product" style="left:12px;top:166px;width:94px;text-align:center">
      <span class="product__name">TrekPulse</span>
      <div style="font-size:6px;font-weight:600;margin-top:3px">fuel economy tuning</div>
      <div style="font-size:7px;margin-top:10px">FLEET SOLUTIONS</div>
    </div>
    <div class="abs" style="left:120px;top:0;width:260px;height:430px;background:var(--charcoal)"></div>
    <div class="abs" style="left:136px;top:16px;width:244px;height:96px;background:var(--blue);"></div>
    <div class="abs title-box" style="left:142px;top:22px;width:238px;height:84px;background:var(--blue-light);padding-top:28px">
      <div style="font-size:10px">REFUEL YOUR</div>
      <div style="font-size:17px">BUSINESS</div>
    </div>
    <div class="photo" role="img" aria-label="Fuel pump nozzle pouring golden fuel" style="left:136px;top:112px;width:244px;height:262px;background:linear-gradient(180deg,#ffffff 0%,#ffffff 42%,#f6d36a 55%,#e9a817 100%)"></div>
    <div class="abs" style="left:60px;top:430px;width:240px;height:107px;background:var(--gold)"></div>
    <div class="abs" style="left:190px;top:430px;width:110px;height:107px;background:var(--gold-soft)"></div>
  </article>
</section>

<div class="label" style="left:822px;top:480px">FRONT COVER</div>
<div class="label" style="left:230px;top:574px">BACK COVER</div>

<section class="spread spread--inside">
  <article class="page page--intro">
    <div class="photo" role="img" aria-label="Row of white fleet vans" style="left:0;top:0;width:380px;height:170px;background:linear-gradient(180deg,#f4f4f4 0%,#d9dcde 60%,#a9aeb2 100%)"></div>
    <div class="abs caption" style="left:12px;top:14px;color:var(--blue);font-size:12px;line-height:1.1;background:rgba(255,255,255,.85);padding:5px 8px">Reduce the cost<br><span style="color:var(--charcoal)">of running<br>your vehicle ›</span></div>
    <div class="abs" style="left:0;top:170px;width:255px;height:260px;background:var(--blue-light)"></div>
    <div class="abs body-copy" style="left:16px;top:182px;width:228px">
      <p>The best way to calculate the potential fuel saving for your business is to conduct a real world trial. Corvane Technologies has conducted trials across a number of vehicles for a set period of time to demonstrate how our TrekPulse technology works. We have found this to be the most effective way of calculating the fuel savings achievable as it takes into account a number of variables, namely:</p>
      <ul>
        <li>Different vehicle types and uses</li>
        <li>Different drivers</li>
        <li>Differing vehicle conditions and age</li>
      </ul>
      <p>All ecotuning software solutions are fully customised for each client and fleet. A return on investment is demonstrated in less than six months.</p>
    </div>
    <div class="abs" style="left:255px;top:170px;width:125px;height:230px;background:var(--grey);padding:12px 10px">
      <div class="col-head" style="color:var(--white)">The Technology</div>
      <ul class="tech-list">
        <li>Custom software uses real-time data from vehicle sensors.</li>
        <li>AIR CONTROLLERS<br>- intake volume<br>- temperature</li>
        <li>FUEL MANAGEMENT<br>- delivery<br>- pressure</li>
        <li>SPARK ADVANCE<br>- optimal degree</li>
        <li>DRIVER CONTROLS<br>- throttle<br>- rev, turbo</li>
      </ul>
    </div>
    <div class="photo" role="img" aria-label="Fleet van beside a blue pool" style="left:0;top:430px;width:380px;height:107px;background:linear-gradient(180deg,#7fc4ea 0%,#2f8fc8 100%)"></div>
    <div class="abs caption" style="left:150px;top:444px;font-size:12px;line-height:1.2;text-align:right;width:218px">Fleetline Van +50BHP<br><span style="font-size:9px">and 75NM of torque</span></div>
  </article>

  <article class="page page--case">
    <div class="abs" style="left:0;top:60px;width:160px;height:370px;background:var(--blue);padding:14px 12px;color:var(--white)">
      <div class="col-head">Fleet Team Support</div>
      <div class="small">Dedicated Fleet Support Team<br><br>High-volume deployment team<br><br>Average file response time 3 mins<br><br>Telephone and email support<br>07:00 – 21:00 Mon – Sat<br><br>Zero warranty failures<br><br>ISO Registered</div>
    </div>
    <div class="abs" style="left:150px;top:0;width:230px;height:370px;background:var(--charcoal)"></div>
    <div class="abs" style="left:164px;top:14px;width:216px;height:342px;background:var(--white)"></div>
    <div class="abs" style="left:164px;top:110px;width:216px;height:246px;background:var(--blue-light)"></div>
    <div class="abs brand" style="left:220px;top:38px;font-size:17px;color:var(--blue)"><span class="brand__mark" style="border-radius:50%"></span>NORTHLINE</div>
    <div class="abs" style="left:164px;top:82px;width:216px;text-align:center;font-family:'Montserrat',sans-serif;font-weight:600;font-size:11px;letter-spacing:1px;color:var(--charcoal)">CASE STUDY</div>
    <div class="abs small" style="left:176px;top:120px;width:194px">
      <b>Corvane – approved and partnered with Northline Fleet to tune 24,000 vehicles in 4 months, delivering estimated savings per year.</b><br><br>
      “Northline is committed to being a responsible business leader, so remapping our vehicles made complete sense. Once we saw what was possible, the business case stacked up.”<br><br>
      – Mark Dalton, Senior Innovation and Design
    </div>
    <div class="photo" role="img" aria-label="Branded fleet van parked outdoors" style="left:164px;top:250px;width:216px;height:106px;background:linear-gradient(180deg,#c9cfc9 0%,#9aa29a 100%)"></div>
    <div class="photo" role="img" aria-label="Support team working at computers in an office" style="left:60px;top:360px;width:200px;height:120px;background:linear-gradient(180deg,#d8c7a6 0%,#9c8464 100%)"></div>
  </article>
</section>

<div class="label" style="left:40px;top:1086px">INSIDE PAGES</div>

</body>
</html>
```